App Design - Job Poise Lantern

We require an App Design for our new App called 'Poise Lantern'. This app is essentially an assistant to help Users prepare for job interviews, to help them get hired. <br/><br/>Users who download the App can view common Questions and Answers, save their favourite responses and also view common Interview Tips. <br/><br/>The vision for our App is for Users who are preparing for an interview (1 week before, 1 day before, even 1 hour before), are able to download, view and educate themselves on common questions and responses, and then be confident to land the job. <br/><br/>Our team has developed wireframes to help highlight what each screen should do and include. Please see attached document, which also highlights key requirements for the experience. Feel free to add/remove/edit what you see on these wireframes. Our preference is that you use Adobe XD please.<br/><br/>In terms of design guidelines, we want the experience to be simple, intuitive and 'memorable' to help Users to remember the questions/responses when they are in the interview. <br/><br/>The final design should communicate 'neat and clean professionalism'; we like the design of: vocatia hub com au<br/><br/>Thank you for reading! Good luck !

Target Market(s)

Professional job seekers

Font styles to use
Sans Serif

Colors

Designer to choose colors to be used in the design.

Requirements
Must have
• Please see my PixelBazaar_UX file that I have uploaded
Nice to have
• Could you also please include some ideas on how we can incorporate Advertising into the app screens

```html
<!DOCTYPE html>
<html lang="en">
<head>
<meta charset="utf-8">
<title>Poise Lantern – App Screens</title>
<link rel="stylesheet" href="https://fonts.googleapis.com/css2?family=Mulish:wght@400;500;600;700;800&display=swap">
<style>
  :root{
    --bg:#eaf2f1;
    --screen:#ffffff;
    --teal:#0e9e98;
    --amber:#f5c451;
    --ink:#262a2e;
    --ink-soft:#4a4f55;
    --muted:#8a8f95;
    --grad:linear-gradient(90deg,var(--teal) 0%,#5fae86 45%,var(--amber) 100%);
  }
  *{box-sizing:border-box;margin:0;padding:0}
  html,body{width:1200px;height:3134px;overflow:hidden}
  body{background:var(--bg);font-family:"Mulish",Arial,sans-serif;color:var(--ink);position:relative}

  .screen{position:absolute;width:390px;background:var(--screen);border-radius:22px;overflow:hidden;box-shadow:0 10px 30px rgba(20,60,60,.12)}
  .screen > *{position:absolute}
  .screen--welcome{left:129px;top:146px;height:870px}
  .screen--tips{left:636px;top:146px;height:870px}
  .screen--questions{left:129px;top:1113px;height:1233px}
  .screen--categories{left:636px;top:1113px;height:996px}
  .screen--tips-alt{left:636px;top:2178px;height:870px}

  .back{left:18px;top:26px;font-size:16px;color:var(--ink);display:flex;align-items:center;gap:4px}
  .back svg{width:9px;height:14px}

  .brand{left:0;right:0;top:88px;display:flex;justify-content:center;align-items:center;gap:10px}
  .brand__mark{width:22px;height:22px;background:var(--teal);border-radius:4px}
  .brand__name{font-size:34px;font-weight:800;color:var(--ink);letter-spacing:.2px}

  .art{border-radius:50%/44%}
  .art--sofa{left:17px;top:219px;width:346px;height:225px;background:radial-gradient(ellipse at 50% 50%,#d7ece7 0%,#7cc4bd 55%,#e9f3f1 100%)}
  .art--bench{left:57px;top:183px;width:268px;height:201px;background:radial-gradient(ellipse at 50% 45%,#f3c45a 0%,#9fc8b2 40%,#e4eeeb 100%)}
  .art--marks{left:72px;top:176px;width:246px;height:219px;background:radial-gradient(ellipse at 50% 50%,#4fc0b2 0%,#f1c04e 38%,#e6edf8 80%)}
  .art--sitting{left:72px;top:183px;width:246px;height:189px;background:radial-gradient(ellipse at 50% 50%,#f2b94c 0%,#3ea596 38%,#e8f0ec 100%)}

  .tagline{left:30px;right:30px;top:525px;text-align:center;font-size:23px;line-height:35px;color:var(--ink-soft)}
  .btn-login{left:83px;top:704px;width:224px;height:51px;border-radius:26px;background:var(--grad);color:#fff;font-weight:700;font-size:19px;display:flex;align-items:center;justify-content:center}
  .ref{right:22px;font-size:16px;color:var(--muted)}

  .heading{left:0;right:0;text-align:center;font-size:26px;font-weight:500;color:var(--ink)}
  .subheading{left:0;right:0;text-align:center;font-size:18px;color:var(--ink-soft)}

  .option{left:23px;width:341px;height:83px;border:2px solid transparent;border-radius:6px;
    background:linear-gradient(#fff,#fff) padding-box,var(--grad) border-box;
    display:flex;align-items:center;font-size:20px;color:var(--ink-soft)}
  .option--nav{justify-content:space-between;padding:0 22px 0 18px}
  .option--nav svg{width:9px;height:15px}
  .option--center{justify-content:center;font-size:21px;color:var(--ink)}

  .btn-all{left:23px;width:341px;height:50px;border-radius:25px;background:var(--grad);color:#fff;font-weight:700;font-size:16px;letter-spacing:.4px;display:flex;align-items:center;justify-content:center}

  .tag{left:23px;top:469px;width:137px;height:44px;background:var(--grad);color:#fff;font-size:18px;font-weight:500;display:flex;align-items:center;justify-content:center;border-radius:3px}
  .question{left:23px;width:341px;border:2px solid transparent;border-radius:6px;
    background:linear-gradient(#fff,#fff) padding-box,var(--grad) border-box;
    padding:0 16px 0 19px;display:flex;align-items:center;font-size:16px;line-height:25px;color:var(--ink)}
</style>
</head>
<body>

<section class="screen screen--welcome">
  <div class="brand"><span class="brand__mark"></span><span class="brand__name">Poise Lantern</span></div>
  <div class="art art--sofa" role="img" aria-label="Illustration of a woman working on a laptop on a sofa with a plant, lamp and cat"></div>
  <p class="tagline">Your guide to the most common interview questions, and the best responses to help you get hired.</p>
  <div class="btn-login">LOGIN</div>
  <span class="ref" style="top:796px">C4</span>
</section>

<section class="screen screen--tips">
  <div class="back"><svg viewBox="0 0 9 14"><path d="M7 1 1 7l6 6" fill="none" stroke="#262a2e" stroke-width="1.6"/></svg>Back</div>
  <div class="brand"><span class="brand__mark"></span><span class="brand__name">Poise Lantern</span></div>
  <div class="art art--bench" role="img" aria-label="Illustration of a person with a laptop on a park bench among leaves"></div>
  <h2 class="heading" style="top:404px">Interview Tips</h2>
  <p class="subheading" style="top:446px">Select your Interview Tips Category</p>
  <div class="option option--nav" style="top:505px">Tips for Before the Interview<svg viewBox="0 0 9 15"><path d="M1 1l6 6.5L1 14" fill="none" stroke="#262a2e" stroke-width="1.6"/></svg></div>
  <div class="option option--nav" style="top:604px">Tips for During the Interview<svg viewBox="0 0 9 15"><path d="M1 1l6 6.5L1 14" fill="none" stroke="#262a2e" stroke-width="1.6"/></svg></div>
  <div class="option option--nav" style="top:707px">Tips for After the Interview<svg viewBox="0 0 9 15"><path d="M1 1l6 6.5L1 14" fill="none" stroke="#262a2e" stroke-width="1.6"/></svg></div>
  <div class="btn-all" style="top:811px">VIEW ALL</div>
</section>

<section class="screen screen--questions">
  <div class="back"><svg viewBox="0 0 9 14"><path d="M7 1 1 7l6 6" fill="none" stroke="#262a2e" stroke-width="1.6"/></svg>Back</div>
  <div class="brand"><span class="brand__mark"></span><span class="brand__name">Poise Lantern</span></div>
  <div class="art art--marks" role="img" aria-label="Illustration of small people beside a large exclamation mark and question mark"></div>
  <h2 class="heading" style="top:417px;text-align:left;left:23px">View Questions &amp; Responses</h2>
  <div class="tag">Behavioral</div>
  <div class="question" style="top:539px;height:144px">1. Give me an example of a new idea or initiative you have suggested to your manager How did you implement this idea?</div>
  <div class="question" style="top:699px;height:144px">2. Give me an example of a time when you made a mistake or didn't deliver on expectations, what happened? What did you learn?</div>
  <div class="question" style="top:858px;height:91px">3. How would ,your colleagues describe you in three words?</div>
  <div class="question" style="top:967px;height:91px">4 What parts of your current role frustrate you?</div>
  <div class="question" style="top:1073px;height:91px">5. What steps would you toke to make an important decision on the job?</div>
  <span class="ref" style="top:1188px">C4</span>
</section>

<section class="screen screen--categories">
  <div class="brand"><span class="brand__mark"></span><span class="brand__name">Poise Lantern</span></div>
  <div class="art art--sitting" role="img" aria-label="Illustration of a woman sitting cross-legged with a laptop among leaves"></div>
  <h2 class="heading" style="top:387px">View Questions &amp; Responses</h2>
  <p class="subheading" style="top:436px">Select your Question Category</p>
  <div class="option option--center" style="top:487px">Behavioral</div>
  <div class="option option--center" style="top:585px">Situational</div>
  <div class="option option--center" style="top:684px">Motivational</div>
  <div class="option option--center" style="top:782px">Technical</div>
  <div class="btn-all" style="top:890px">VIEW ALL</div>
  <span class="ref" style="top:957px">C4</span>
</section>

<section class="screen screen--tips-alt">
  <div class="back"><svg viewBox="0 0 9 14"><path d="M7 1 1 7l6 6" fill="none" stroke="#262a2e" stroke-width="1.6"/></svg>Back</div>
  <div class="brand"><span class="brand__mark"></span><span class="brand__name">Poise Lantern</span></div>
  <div class="art art--bench" role="img" aria-label="Illustration of a person with a laptop on a park bench among leaves"></div>
  <h2 class="heading" style="top:404px">Interview Tips</h2>
  <p class="subheading" style="top:446px">Select your Interview Tips Category</p>
  <div class="option option--nav" style="top:505px">Tips for Before the Interview<svg viewBox="0 0 9 15"><path d="M1 1l6 6.5L1 14" fill="none" stroke="#262a2e" stroke-width="1.6"/></svg></div>
  <div class="option option--nav" style="top:604px">Tips for During the Interview<svg viewBox="0 0 9 15"><path d="M1 1l6 6.5L1 14" fill="none" stroke="#262a2e" stroke-width="1.6"/></svg></div>
  <div class="option option--nav" style="top:707px">Tips for After the Interview<svg viewBox="0 0 9 15"><path d="M1 1l6 6.5L1 14" fill="none" stroke="#262a2e" stroke-width="1.6"/></svg></div>
  <div class="btn-all" style="top:811px">VIEW ALL</div>
</section>

</body>
</html>
```